Web Designer criação do designer da loja

preciso que faça o modelo de como seria a loja virtual ( ecommerce ) apenas o desenho da pagina ja possuo o logo e preciso do desenho de como sera a loja virtual e comercializa produtos de informatica e telefonia quero se sigam as regras das cores do logo estou enviando duas logos com os fundo diferentes de preferencia criar o projeto no fundo laranja como consta no logo enviado

Target Market(s)

ecommerce designers

Number of Pages Required

1 page

Font styles to use
Sans Serif

Requirements
Must have
• meu projeto deve-se comparar com as lojas virtuais do momento

```html
<!DOCTYPE html>
<html lang="en">
<head>
<meta charset="UTF-8">
<title>Voltrix Store</title>
<link href="https://fonts.googleapis.com/css2?family=Source+Sans+3:wght@400;600;700&display=swap" rel="stylesheet">
<style>
:root{
  --orange:#ff6a00;
  --orange-deep:#ff4d00;
  --orange-light:#ff8a1f;
  --ink:#333333;
  --muted:#666666;
  --rule:#d9d9d9;
  --card:#eceded;
  --footer:#343434;
  --footer-bottom:#2c2c2c;
  --footer-text:#bdbdbd;
  --white:#ffffff;
}
*{margin:0;padding:0;box-sizing:border-box}
html,body{width:848px;height:1200px;overflow:hidden}
body{font-family:"Source Sans 3",sans-serif;color:var(--ink);background:var(--white);position:relative}
.abs{position:absolute}

.topbar{left:0;top:0;width:848px;height:61px;background:var(--orange)}
.top-links{left:153px;top:24px;font-size:9.5px;font-weight:700;color:var(--white)}
.top-links span{margin:0 4px}
.brand{left:0;width:848px;top:15px;text-align:center;font-size:22px;font-weight:700;color:var(--white);letter-spacing:.5px}
.currency{left:633px;top:24px;font-size:9.5px;font-weight:700;color:var(--white)}
.currency svg{vertical-align:middle;margin-left:4px}

.navbar{left:0;top:61px;width:848px;height:28px;background:var(--white);box-shadow:0 1px 2px rgba(0,0,0,.25)}
.nav-item{top:73px;font-size:8.5px;font-weight:700;letter-spacing:.6px;color:#444;text-transform:uppercase}
.nav-item.active{color:var(--orange)}
.caret{font-size:6px;margin-left:3px;vertical-align:1px}
.nav-tools{left:607px;top:70px;display:flex;align-items:center;gap:8px;font-size:9px;font-weight:700;color:#444}
.nav-tools .divider{width:1px;height:12px;background:var(--rule)}

.hero{left:0;top:89px;width:848px;height:272px;background:linear-gradient(180deg,var(--orange-light) 0%,var(--orange) 55%,var(--orange-deep) 100%)}
.hero-visual{left:154px;top:113px;width:234px;height:218px;border-radius:6px;background:radial-gradient(ellipse at 45% 45%,#2a2f45 0%,#141416 60%,rgba(20,20,22,0) 100%)}
.hero-title{left:437px;top:153px;font-size:28px;font-weight:700;color:var(--white)}
.hero-text{left:437px;top:190px;width:272px;font-size:9px;line-height:15.3px;color:var(--white)}
.hero-btn{left:436px;top:254px;width:119px;height:32px;background:#e6e6e6;border-radius:2px;display:flex;align-items:center;justify-content:center;font-size:12.5px;font-weight:700;color:#555;letter-spacing:.3px}
.hero-arrow{top:214px}

.section-title{left:0;width:848px;text-align:center;font-size:13px;font-weight:700;color:#444}
.section-rule{left:153px;width:540px;height:1px;background:var(--rule)}
.section-notch{left:418px;width:12px;height:7px}

.card{width:128px;height:146px;background:var(--card);border:1px solid #dedede}
.card-media{position:absolute;left:14px;top:14px;width:98px;height:110px;border-radius:4px}
.media-phone{background:linear-gradient(135deg,#5a6272,#a9b6c2 60%,#dfe5ea)}
.media-tower{background:radial-gradient(ellipse at 50% 50%,#2b3a6e 0%,#151515 65%,rgba(21,21,21,0) 100%)}
.media-tablet{background:linear-gradient(180deg,#202020 0%,#5e6c55 40%,#b77a3a 70%,#202020 100%)}
.media-desk{background:radial-gradient(ellipse at 45% 50%,#263566 0%,#161616 65%,rgba(22,22,22,0) 100%)}
.cart-bar{position:absolute;left:0;bottom:0;width:100%;height:33px;background:#555;color:var(--white);font-size:11.5px;display:flex;align-items:center;justify-content:center}
.product-name{width:128px;text-align:center;font-size:9.5px;color:#555}
.product-price{width:128px;text-align:center;font-size:9.5px;font-weight:700;color:#333}
.pager{width:20px;height:20px;border:1px solid #c8c8c8;border-radius:50%;display:flex;align-items:center;justify-content:center;background:var(--white)}

.footer{left:0;top:972px;width:848px;height:159px;background:var(--footer)}
.footer-col{top:1008px}
.footer-col h3{font-size:13px;font-weight:700;color:#d6d6d6;margin-bottom:6px}
.footer-col li{list-style:none;font-size:7.6px;line-height:16.6px;color:var(--footer-text)}
.footer-bottom{left:0;top:1131px;width:848px;height:61px;background:var(--footer-bottom);border-top:1px solid #444}
.footer-brand{left:154px;top:1143px;width:101px;height:37px;background:var(--orange);display:flex;align-items:center;justify-content:center;font-size:12px;font-weight:700;color:var(--white)}
.footer-links{left:263px;top:1146px;font-size:8px;color:var(--footer-text)}
.footer-links span{margin:0 5px}
.copyright{left:263px;top:1164px;font-size:8px;color:var(--orange)}
.base-strip{left:0;top:1192px;width:848px;height:8px;background:#111}
</style>
</head>
<body>

<header>
  <div class="abs topbar"></div>
  <div class="abs top-links">My Store<span>|</span>My Account<span>|</span>Orders</div>
  <div class="abs brand">Voltrix</div>
  <div class="abs currency">US Dollars $<svg width="6" height="4" viewBox="0 0 6 4"><path d="M0 0h6L3 4z" fill="#fff"/></svg></div>

  <nav class="abs navbar"></nav>
  <div class="abs nav-item active" style="left:153px">Home</div>
  <div class="abs nav-item" style="left:198px">About</div>
  <div class="abs nav-item" style="left:254px">Electronics<span class="caret">▼</span></div>
  <div class="abs nav-item" style="left:339px">Computers<span class="caret">▼</span></div>
  <div class="abs nav-item" style="left:423px">New Products<span class="caret">▼</span></div>
  <div class="abs nav-item" style="left:521px">Contact</div>
  <div class="abs nav-tools">
    <svg width="9" height="9" viewBox="0 0 10 10"><circle cx="4" cy="4" r="3" fill="none" stroke="#555" stroke-width="1.3"/><path d="M6.3 6.3L9 9" stroke="#555" stroke-width="1.4"/></svg>
    <span class="divider"></span>
    <svg width="8" height="10" viewBox="0 0 8 10"><path d="M2 3V2a2 2 0 0 1 4 0v1" fill="none" stroke="#333" stroke-width="1"/><rect x="0.5" y="3" width="7" height="7" fill="#333"/></svg>
    <span>Cart empty</span>
  </div>
</header>

<section>
  <div class="abs hero"></div>
  <div class="abs hero-visual" role="img" aria-label="Black gaming tower with blue lights next to a widescreen monitor"></div>
  <h1 class="abs hero-title">Best Quality</h1>
  <p class="abs hero-text">Lorem ipsum dolor sit amet, consectetur adipisicing elit, sed do eiusmod tempor incididunt ut labore et dolore magna aliqua. Ut enim ad minim veniam, quis nostrud exercitation ullamco.</p>
  <div class="abs hero-btn">SHOP NOW</div>
  <svg class="abs hero-arrow" style="left:20px" width="18" height="24" viewBox="0 0 18 24"><path d="M15 2L4 12l11 10" fill="none" stroke="#ffa040" stroke-width="4"/></svg>
  <svg class="abs hero-arrow" style="left:811px" width="18" height="24" viewBox="0 0 18 24"><path d="M3 2l11 10L3 22" fill="none" stroke="#ffa040" stroke-width="4"/></svg>
</section>

<section>
  <h2 class="abs section-title" style="top:387px">Featured Products</h2>
  <div class="abs section-rule" style="top:409px"></div>
  <svg class="abs section-notch" style="top:409px" viewBox="0 0 12 7"><path d="M0 0h12L6 7z" fill="#cfcfcf"/></svg>

  <div class="abs card" style="left:153px;top:437px"><div class="card-media media-phone" role="img" aria-label="Smartphone with stylus shown front and back"></div><div class="cart-bar">Add to cart</div></div>
  <div class="abs card" style="left:291px;top:437px"><div class="card-media media-tower" role="img" aria-label="Black gaming computer tower"></div></div>
  <div class="abs card" style="left:428px;top:437px"><div class="card-media media-tablet" role="img" aria-label="Tablet displaying a photo gallery"></div></div>
  <div class="abs card" style="left:566px;top:437px"><div class="card-media media-desk" role="img" aria-label="Computer tower with a widescreen monitor"></div></div>

  <div class="abs product-name" style="left:153px;top:599px">Electronic Set</div><div class="abs product-price" style="left:153px;top:615px">$170.00</div>
  <div class="abs product-name" style="left:291px;top:599px">Electronic Set</div><div class="abs product-price" style="left:291px;top:615px">$170.00</div>
  <div class="abs product-name" style="left:428px;top:599px">Electronic Set</div><div class="abs product-price" style="left:428px;top:615px">$170.00</div>
  <div class="abs product-name" style="left:566px;top:599px">Electronic Set</div><div class="abs product-price" style="left:566px;top:615px">$170.00</div>

  <div class="abs pager" style="left:399px;top:625px"><svg width="6" height="8" viewBox="0 0 6 8"><path d="M5 0.5L1.5 4 5 7.5" fill="none" stroke="#999" stroke-width="1.2"/></svg></div>
  <div class="abs pager" style="left:428px;top:625px"><svg width="6" height="8" viewBox="0 0 6 8"><path d="M1 0.5L4.5 4 1 7.5" fill="none" stroke="#999" stroke-width="1.2"/></svg></div>
</section>

<section>
  <h2 class="abs section-title" style="top:687px">New Products</h2>
  <div class="abs section-rule" style="top:708px"></div>
  <svg class="abs section-notch" style="top:708px" viewBox="0 0 12 7"><path d="M0 0h12L6 7z" fill="#cfcfcf"/></svg>

  <div class="abs card" style="left:153px;top:736px"><div class="card-media media-phone" role="img" aria-label="Smartphone with stylus shown front and back"></div><div class="cart-bar">Add to cart</div></div>
  <div class="abs card" style="left:291px;top:736px"><div class="card-media media-tower" role="img" aria-label="Black gaming computer tower"></div></div>
  <div class="abs card" style="left:428px;top:736px"><div class="card-media media-tablet" role="img" aria-label="Tablet displaying a photo gallery"></div></div>
  <div class="abs card" style="left:566px;top:736px"><div class="card-media media-desk" role="img" aria-label="Computer tower with a widescreen monitor"></div></div>

  <div class="abs product-name" style="left:153px;top:898px">Electronic Set</div><div class="abs product-price" style="left:153px;top:914px">$170.00</div>
  <div class="abs product-name" style="left:291px;top:898px">Electronic Set</div><div class="abs product-price" style="left:291px;top:914px">$170.00</div>
  <div class="abs product-name" style="left:428px;top:898px">Electronic Set</div><div class="abs product-price" style="left:428px;top:914px">$170.00</div>
  <div class="abs product-name" style="left:566px;top:898px">Electronic Set</div><div class="abs product-price" style="left:566px;top:914px">$170.00</div>

  <div class="abs pager" style="left:399px;top:924px"><svg width="6" height="8" viewBox="0 0 6 8"><path d="M5 0.5L1.5 4 5 7.5" fill="none" stroke="#999" stroke-width="1.2"/></svg></div>
  <div class="abs pager" style="left:428px;top:924px"><svg width="6" height="8" viewBox="0 0 6 8"><path d="M1 0.5L4.5 4 1 7.5" fill="none" stroke="#999" stroke-width="1.2"/></svg></div>
</section>

<footer>
  <div class="abs footer"></div>
  <div class="abs footer-col" style="left:153px"><h3>About Us</h3><ul><li>About us</li><li>Delivery</li><li>FAQs</li><li>Contacts</li><li>Online store</li></ul></div>
  <div class="abs footer-col" style="left:279px"><h3>My Account</h3><ul><li>Order History</li><li>Advance Search</li><li>Create Account</li><li>Category layout</li><li>Product layout</li></ul></div>
  <div class="abs footer-col" style="left:424px"><h3>Information</h3><ul><li>Order Details</li><li>Payment Details</li><li>Shipping Details</li><li>Static Details</li><li>Product Returns</li></ul></div>
  <div class="abs footer-col" style="left:556px"><h3>Contact Us</h3><ul><li>Voltrix Ltda, 18 Rua das Palmeiras</li><li>Centro 04500, Lisboa,</li><li>Portugal-21000,</li><li>0800-555-210</li><li>vendas@voltrix-loja.com</li></ul></div>

  <div class="abs footer-bottom"></div>
  <div class="abs footer-brand">Voltrix</div>
  <div class="abs footer-links">My Store<span>|</span>My Account<span>|</span>Orders<span>|</span>Home</div>
  <div class="abs copyright">Voltrix © 2015.&nbsp;&nbsp;All Rights Reserved.</div>
  <div class="abs base-strip"></div>
</footer>

</body>
</html>
```